5 year service award card*

I'm attaching a celebration type card in which I need a new card similar made but with KVR logo's on it instead.

Colors

Designer to choose colors to be used in the design.

```html
<!DOCTYPE html>
<html lang="en">
<head>
<meta charset="utf-8">
<title>KVR Solutions – 5 Years Service Award</title>
<link rel="stylesheet" href="https://fonts.googleapis.com/css2?family=Great+Vibes&family=Lato:wght@400;700;900&display=swap">
<style>
  :root {
    --brand-blue: #3a7cc4;
    --text-grey: #6a6a6a;
    --rule-grey: #c6c6c6;
    --paper: #ffffff;
    --backdrop: #ececec;
    --signature-tint: #e4e6ea;
  }
  * { margin: 0; padding: 0; box-sizing: border-box; }
  html, body {
    width: 1090px;
    height: 1200px;
    overflow: hidden;
    background: var(--backdrop);
    font-family: "Lato", sans-serif;
  }
  .award-card {
    position: absolute;
    left: 145px;
    top: 40px;
    width: 800px;
    height: 1120px;
    background: var(--paper);
    border: 7px solid var(--brand-blue);
  }
  .inner-frame {
    position: absolute;
    inset: 21px;
    border: 2px solid var(--brand-blue);
  }
  .corner-ornament {
    position: absolute;
    width: 60px;
    height: 60px;
    background: var(--brand-blue);
  }
  .corner-ornament.top-left { left: 4px; top: 8px; }
  .corner-ornament.top-right { right: 4px; top: 8px; }
  .corner-ornament.bottom-left { left: 4px; bottom: 8px; }
  .corner-ornament.bottom-right { right: 4px; bottom: 8px; }

  .centered {
    position: absolute;
    left: 0;
    right: 0;
    text-align: center;
  }
  .brand-name {
    top: 90px;
    display: flex;
    justify-content: center;
    align-items: center;
    gap: 16px;
    font-weight: 900;
    font-size: 46px;
    letter-spacing: 2px;
    color: var(--brand-blue);
    line-height: 1;
  }
  .brand-square {
    width: 40px;
    height: 40px;
    background: var(--brand-blue);
  }
  .award-title {
    top: 205px;
    font-family: "Great Vibes", cursive;
    font-size: 74px;
    line-height: 82px;
    color: var(--brand-blue);
  }
  .body-text {
    font-size: 26px;
    line-height: 32px;
    color: var(--text-grey);
  }
  .presented-to { top: 456px; }
  .recipient-line, .signature-line {
    position: absolute;
    left: 284px;
    width: 218px;
    height: 2px;
    background: var(--rule-grey);
  }
  .recipient-line { top: 554px; }
  .recognition { top: 613px; }
  .organisation {
    top: 725px;
    font-size: 27px;
    font-weight: 700;
    color: var(--brand-blue);
  }
  .signature-area {
    position: absolute;
    left: 276px;
    top: 855px;
    width: 232px;
    height: 56px;
    background: var(--signature-tint);
  }
  .signature-line { top: 923px; }
  .signatory { top: 941px; }
  .signatory .signatory-name { text-transform: uppercase; }
</style>
</head>
<body>
  <main class="award-card">
    <div class="inner-frame"></div>
    <div class="corner-ornament top-left" role="img" aria-label="Geometric corner ornament"></div>
    <div class="corner-ornament top-right" role="img" aria-label="Geometric corner ornament"></div>
    <div class="corner-ornament bottom-left" role="img" aria-label="Geometric corner ornament"></div>
    <div class="corner-ornament bottom-right" role="img" aria-label="Geometric corner ornament"></div>

    <div class="centered brand-name"><span class="brand-square"></span><span>KVR SOLUTIONS</span></div>

    <h1 class="centered award-title">5 Years Service<br>Award</h1>

    <p class="centered body-text presented-to">Presented To</p>
    <div class="recipient-line"></div>

    <p class="centered body-text recognition">In Recognition of 5 years of<br>invaluable voluntary service to</p>
    <p class="centered body-text organisation">Bright Horizon Charity</p>

    <div class="signature-area" role="img" aria-label="Handwritten signature of the president"></div>
    <div class="signature-line"></div>
    <p class="centered body-text signatory">
      <span class="signatory-name">Mr. Daniel Hart</span><br>
      President, KVR Solutions<br>
      1 December 2019
    </p>
  </main>
</body>
</html>
```